KindCircle.net Website Re-Skin / Re-Design (Go to www.westandkind.net)

A more detailed scope of works is outlined in the attached document.

Basically, we require a clean, crisp, contemporary, professional colour re-re-skin / re-design of the www.westandkind.net website, a redesign of the user profile pictures on the website, and (possible) logo re-design to match your colour design re-skin.

No major structural design changes of the website are planned at this stage so the changes need to be easily re-coded by the programmer, so keep it limited to colour combinations, icon locations, colours, font size and colours etc.

The simpler and the easier the re-skin the better.
Updates

Dear Designers, For some reason we are having an issue with the test www.kindcircle.net website being displayed. For an alternative, please go to WWW.WESTANDKIND.NET if you wish to view the website. Regards, Marlo

Logo Text

KindCircle

Number of Pages Required

1 page

Font styles to use
Sans Serif

Colors

Designer to choose colors to be used in the design.

```html
<!DOCTYPE html>
<html lang="en">
<head>
<meta charset="utf-8">
<title>KindCircle – Members</title>
<link href="https://fonts.googleapis.com/css2?family=Open+Sans:wght@400;600;700&display=swap" rel="stylesheet">
<style>
:root{
  --ink:#1f2a2b;
  --topbar:#222c2d;
  --green:#3c9a3b;
  --green-dark:#2f7f2f;
  --page:#f1f3f1;
  --card:#ffffff;
  --line:#dfe3df;
  --muted:#7a8582;
  --photo-a:#2e3a36;
  --photo-b:#6d7f6a;
  --white:#ffffff;
}
*{box-sizing:border-box;margin:0;padding:0}
html,body{width:781px;height:1200px;overflow:hidden}
body{font-family:"Open Sans",Arial,sans-serif;background:var(--page);color:var(--ink);font-size:6px;position:relative}

.topbar{height:28px;background:var(--topbar);display:flex;align-items:center;padding:0 22px;gap:10px}
.search{width:120px;height:14px;border-radius:7px;background:#3a4546;color:#aab3b2;font-size:6px;padding:0 8px;display:flex;align-items:center;gap:4px}
.brand{flex:1;display:flex;justify-content:center;align-items:center;gap:4px;color:var(--green);font-weight:700;font-size:14px}
.brand i{width:12px;height:12px;border-radius:50%;background:var(--green);display:block}
.account{display:flex;gap:12px;color:#d8dedd;font-size:6px;font-weight:600;letter-spacing:.3px}

.mainnav{height:16px;background:var(--green);display:flex;align-items:center;padding:0 60px;gap:24px;color:var(--white);font-size:6.5px;font-weight:600}
.mainnav .actions{margin-left:auto;border:1px solid var(--white);border-radius:7px;padding:1px 10px}

.hero{height:64px;background:linear-gradient(100deg,#1e2a24,#3d4c3f 55%,#26302b);display:flex;align-items:center;padding:0 56px;gap:20px}
.hero p{flex:1;color:var(--white);font-weight:700;font-size:11px;line-height:1.3;max-width:420px}
.hero .btn{border:1px solid var(--white);border-radius:12px;color:var(--white);font-weight:600;font-size:8px;padding:6px 16px}

.members{position:absolute;top:118px;left:16px;width:749px;height:988px;display:flex;gap:7px}
.col{flex:1;display:flex;flex-direction:column;gap:7px}
.card{flex:auto;background:var(--card);border:1px solid var(--line);border-radius:2px;display:flex;flex-direction:column;padding:3px}
.photo{flex:1;min-height:46px;background:linear-gradient(160deg,var(--photo-b),var(--photo-a));border-radius:1px;display:flex;align-items:flex-end;justify-content:center;padding-bottom:5px}
.photo.light{background:linear-gradient(160deg,#9aa79a,#4b5a4e)}
.tag{color:var(--white);font-weight:700;font-size:6px;text-align:center;letter-spacing:.3px;line-height:1.2}
.tag small{display:block;font-size:4.5px;font-weight:600;color:#cfe8cf}
.info{padding:4px 2px 3px;line-height:1.35}
.info b{display:block;font-size:6.5px;font-weight:600}
.info span{display:block;color:var(--muted);font-size:5.5px}
.invites{list-style:none;border-top:1px solid var(--line)}
.invites li{display:flex;align-items:center;gap:3px;padding:2px;color:var(--muted);font-size:5px;border-bottom:1px solid var(--line)}
.invites li::before{content:"";width:8px;height:8px;border-radius:50%;background:#8c9a8e;flex:none}
.badges{display:flex;gap:3px;padding:3px 2px 1px}
.badges i{width:22px;height:6px;border-radius:3px;background:#e4ece4;display:block}
.badges i:first-child{background:#cfe6cf}

.more{position:absolute;top:1108px;left:50%;transform:translateX(-50%);width:18px;height:14px}
.footer{position:absolute;left:0;right:0;bottom:0;height:70px;background:var(--green);color:var(--white);text-align:center;padding-top:20px;font-size:6.5px}
.social{display:flex;justify-content:center;gap:5px;margin-top:8px}
.social i{width:12px;height:12px;border-radius:50%;border:1px solid var(--white);display:block}
</style>
</head>
<body>

<header class="topbar">
  <div class="search">
    <svg width="6" height="6" viewBox="0 0 10 10"><circle cx="4" cy="4" r="3" fill="none" stroke="#aab3b2" stroke-width="1.5"/><line x1="6.5" y1="6.5" x2="9.5" y2="9.5" stroke="#aab3b2" stroke-width="1.5"/></svg>
    Enter Keyword
  </div>
  <div class="brand"><i></i>KindCircle</div>
  <nav class="account"><span>REGISTER ▾</span><span>LOGIN ▾</span><span>USEFUL ▾</span></nav>
</header>

<nav class="mainnav">
  <span>PEOPLE</span><span>ORGANIZATIONS</span><span>GROUPS</span><span>UNCOMMITTED</span>
  <span class="actions">ACTIONS</span>
</nav>

<section class="hero" role="img" aria-label="Dark forest landscape banner">
  <p>People and organizations choosing to do business in an ethical, mature, collaborative and supportive way.</p>
  <span class="btn">REGISTER</span>
  <span class="btn">LOG IN</span>
</section>

<main class="members">
  <div class="col">
    <article class="card"><div class="photo" role="img" aria-label="Member portrait"><span class="tag">MARLO QUENBY<small>STANDS KIND</small></span></div><div class="info"><b>Marlo Quenby</b><span>Director</span><span>Greenleaf Co</span></div><ul class="invites"><li>Invited by Nadia Pell</li><li>Invited by Owen Dale</li></ul><div class="badges"><i></i><i></i></div></article>
    <article class="card"><div class="photo light" role="img" aria-label="Member portrait"><span class="tag">OWEN DALE<small>STANDS KIND</small></span></div><div class="info"><b>Owen Dale</b><span>Store lead</span><span>Brightway</span></div><ul class="invites"><li>Invited by Lena Voss</li></ul><div class="badges"><i></i><i></i></div></article>
    <article class="card"><div class="photo" role="img" aria-label="Member portrait"><span class="tag">MARLO QUENBY<small>STANDS KIND</small></span></div><div class="info"><b>Marlo Quenby</b><span>Director</span><span>Greenleaf Co</span></div><ul class="invites"><li>Invited by Corin Vale</li><li>Invited by Tessa Moor</li><li>Invited by Alden Roy</li></ul><div class="badges"><i></i><i></i></div></article>
    <article class="card"><div class="photo light" role="img" aria-label="Member portrait"><span class="tag">MARLO QUENBY<small>STANDS KIND</small></span></div><div class="info"><b>Marlo Quenby</b><span>Director</span><span>Greenleaf Co</span></div><ul class="invites"><li>Invited by Ines Hart</li><li>Invited by Nadia Pell</li></ul><div class="badges"><i></i><i></i></div></article>
    <article class="card"><div class="photo" role="img" aria-label="Member portrait"><span class="tag">ALDEN ROY<small>STANDS KIND</small></span></div><div class="info"><b>Alden Roy</b><span>Lab tester</span><span>Tolvane</span></div><ul class="invites"><li>Invited by Mira Sol</li></ul><div class="badges"><i></i><i></i></div></article>
  </div>

  <div class="col">
    <article class="card"><div class="photo light" role="img" aria-label="Member portrait"><span class="tag">PRIYA LUND<small>STANDS KIND</small></span></div><div class="info"><b>Priya Lund</b><span>Web builder</span><span>Keystone</span></div><ul class="invites"><li>Invited by Nadia Pell</li><li>Invited by Owen Dale</li><li>Invited by Lena Voss</li></ul><div class="badges"><i></i><i></i></div></article>
    <article class="card"><div class="photo" role="img" aria-label="Member portrait"><span class="tag">INES HART<small>STANDS KIND</small></span></div><div class="info"><b>Ines Hart</b><span>Sales lead</span><span>Northfield</span></div><ul class="invites"><li>Invited by Corin Vale</li></ul><div class="badges"><i></i><i></i></div></article>
    <article class="card"><div class="photo light" role="img" aria-label="Member portrait"><span class="tag">MARLO QUENBY<small>STANDS KIND</small></span></div><div class="info"><b>Marlo Quenby</b><span>Director</span><span>Greenleaf Co</span></div><ul class="invites"><li>Invited by Tessa Moor</li><li>Invited by Alden Roy</li></ul><div class="badges"><i></i><i></i></div></article>
    <article class="card"><div class="photo" role="img" aria-label="Member portrait"><span class="tag">PRIYA LUND<small>STANDS KIND</small></span></div><div class="info"><b>Priya Lund</b><span>Web builder</span><span>Keystone</span></div><ul class="invites"><li>Invited by Ines Hart</li><li>Invited by Mira Sol</li></ul><div class="badges"><i></i><i></i></div></article>
    <article class="card"><div class="photo light" role="img" aria-label="Member portrait"><span class="tag">PRIYA LUND<small>STANDS KIND</small></span></div><div class="info"><b>Priya Lund</b><span>Web builder</span><span>Keystone</span></div><ul class="invites"><li>Invited by Owen Dale</li></ul><div class="badges"><i></i><i></i></div></article>
  </div>

  <div class="col">
    <article class="card"><div class="photo" role="img" aria-label="Member portrait"><span class="tag">NADIA PELL<small>STANDS KIND</small></span></div><div class="info"><b>Nadia Pell</b><span>Director</span><span>Greenleaf Co</span></div><ul class="invites"><li>Invited by Marlo Quenby</li><li>Invited by Lena Voss</li></ul><div class="badges"><i></i><i></i></div></article>
    <article class="card"><div class="photo light" role="img" aria-label="Member portrait"><span class="tag">EZRA QUILL<small>STANDS KIND</small></span></div><div class="info"><b>Ezra Quill</b><span>Planner</span><span>Corvia</span></div><ul class="invites"><li>Invited by Corin Vale</li><li>Invited by Tessa Moor</li><li>Invited by Ines Hart</li></ul><div class="badges"><i></i><i></i></div></article>
    <article class="card"><div class="photo" role="img" aria-label="Member portrait"><span class="tag">LENA VOSS<small>STANDS KIND</small></span></div><div class="info"><b>Lena Voss</b><span>Ward nurse</span><span>Westmere</span></div><ul class="invites"><li>Invited by Alden Roy</li></ul><div class="badges"><i></i><i></i></div></article>
    <article class="card"><div class="photo light" role="img" aria-label="Member portrait"><span class="tag">ALDEN ROY<small>STANDS KIND</small></span></div><div class="info"><b>Alden Roy</b><span>Lab tester</span><span>Tolvane</span></div><ul class="invites"><li>Invited by Nadia Pell</li><li>Invited by Mira Sol</li></ul><div class="badges"><i></i><i></i></div></article>
    <article class="card"><div class="photo" role="img" aria-label="Member portrait"><span class="tag">ALDEN ROY<small>STANDS KIND</small></span></div><div class="info"><b>Alden Roy</b><span>Lab tester</span><span>Tolvane</span></div><ul class="invites"><li>Invited by Owen Dale</li></ul><div class="badges"><i></i><i></i></div></article>
  </div>

  <div class="col">
    <article class="card"><div class="photo light" role="img" aria-label="Member portrait"><span class="tag">CORIN VALE<small>STANDS KIND</small></span></div><div class="info"><b>Corin Vale</b><span>Director</span><span>Greenleaf Co</span></div><ul class="invites"><li>Invited by Lena Voss</li><li>Invited by Ines Hart</li></ul><div class="badges"><i></i><i></i></div></article>
    <article class="card"><div class="photo" role="img" aria-label="Member portrait"><span class="tag">LENA VOSS<small>STANDS KIND</small></span></div><div class="info"><b>Lena Voss</b><span>Ward nurse</span><span>Westmere</span></div><ul class="invites"><li>Invited by Tessa Moor</li></ul><div class="badges"><i></i><i></i></div></article>
    <article class="card"><div class="photo light" role="img" aria-label="Member portrait"><span class="tag">OWEN DALE<small>STANDS KIND</small></span></div><div class="info"><b>Owen Dale</b><span>Store lead</span><span>Brightway</span></div><ul class="invites"><li>Invited by Marlo Quenby</li><li>Invited by Alden Roy</li><li>Invited by Corin Vale</li></ul><div class="badges"><i></i><i></i></div></article>
    <article class="card"><div class="photo" role="img" aria-label="Member portrait"><span class="tag">PRIYA LUND<small>STANDS KIND</small></span></div><div class="info"><b>Priya Lund</b><span>Web builder</span><span>Keystone</span></div><ul class="invites"><li>Invited by Nadia Pell</li></ul><div class="badges"><i></i><i></i></div></article>
    <article class="card"><div class="photo light" role="img" aria-label="Member portrait"><span class="tag">LENA VOSS<small>STANDS KIND</small></span></div><div class="info"><b>Lena Voss</b><span>Ward nurse</span><span>Westmere</span></div><ul class="invites"><li>Invited by Mira Sol</li><li>Invited by Owen Dale</li></ul><div class="badges"><i></i><i></i></div></article>
  </div>

  <div class="col">
    <article class="card"><div class="photo" role="img" aria-label="Member portrait"><span class="tag">TESSA MOOR<small>STANDS KIND</small></span></div><div class="info"><b>Tessa Moor</b><span>Director</span><span>Greenleaf Co</span></div><ul class="invites"><li>Invited by Ines Hart</li></ul><div class="badges"><i></i><i></i></div></article>
    <article class="card"><div class="photo light" role="img" aria-label="Member portrait"><span class="tag">MIRA SOL<small>STANDS KIND</small></span></div><div class="info"><b>Mira Sol</b><span>Bookkeeper</span><span>Harbrook</span></div><ul class="invites"><li>Invited by Lena Voss</li><li>Invited by Corin Vale</li></ul><div class="badges"><i></i><i></i></div></article>
    <article class="card"><div class="photo" role="img" aria-label="Member portrait"><span class="tag">DANA WHIT<small>STANDS KIND</small></span></div><div class="info"><b>Dana Whit</b><span>Project lead</span><span>Harbrook</span></div><ul class="invites"><li>Invited by Tessa Moor</li><li>Invited by Alden Roy</li><li>Invited by Nadia Pell</li></ul><div class="badges"><i></i><i></i></div></article>
    <article class="card"><div class="photo light" role="img" aria-label="Member portrait"><span class="tag">SAMI ROWE<small>STANDS KIND</small></span></div><div class="info"><b>Sami Rowe</b><span>Illustrator</span><span>Keystone</span></div><ul class="invites"><li>Invited by Marlo Quenby</li></ul><div class="badges"><i></i><i></i></div></article>
    <article class="card"><div class="photo" role="img" aria-label="Member portrait"><span class="tag">LENA VOSS<small>STANDS KIND</small></span></div><div class="info"><b>Lena Voss</b><span>Ward nurse</span><span>Westmere</span></div><ul class="invites"><li>Invited by Owen Dale</li><li>Invited by Mira Sol</li></ul><div class="badges"><i></i><i></i></div></article>
  </div>

  <div class="col">
    <article class="card"><div class="photo light" role="img" aria-label="Member portrait"><span class="tag">ALDEN ROY<small>STANDS KIND</small></span></div><div class="info"><b>Alden Roy</b><span>Lab tester</span><span>Tolvane</span></div><ul class="invites"><li>Invited by Nadia Pell</li><li>Invited by Ines Hart</li></ul><div class="badges"><i></i><i></i></div></article>
    <article class="card"><div class="photo" role="img" aria-label="Member portrait"><span class="tag">YUSUF OKAFOR<small>STANDS KIND</small></span></div><div class="info"><b>Yusuf Okafor</b><span>Systems planner</span><span>Corvia</span></div><ul class="invites"><li>Invited by Lena Voss</li></ul><div class="badges"><i></i><i></i></div></article>
    <article class="card"><div class="photo light" role="img" aria-label="Member portrait"><span class="tag">PRIYA LUND<small>STANDS KIND</small></span></div><div class="info"><b>Priya Lund</b><span>Web builder</span><span>Keystone</span></div><ul class="invites"><li>Invited by Corin Vale</li><li>Invited by Tessa Moor</li><li>Invited by Owen Dale</li></ul><div class="badges"><i></i><i></i></div></article>
    <article class="card"><div class="photo" role="img" aria-label="Member portrait"><span class="tag">OWEN DALE<small>STANDS KIND</small></span></div><div class="info"><b>Owen Dale</b><span>Store lead</span><span>Brightway</span></div><ul class="invites"><li>Invited by Alden Roy</li></ul><div class="badges"><i></i><i></i></div></article>
    <article class="card"><div class="photo light" role="img" aria-label="Member portrait"><span class="tag">ALDEN ROY<small>STANDS KIND</small></span></div><div class="info"><b>Alden Roy</b><span>Lab tester</span><span>Tolvane</span></div><ul class="invites"><li>Invited by Mira Sol</li><li>Invited by Marlo Quenby</li></ul><div class="badges"><i></i><i></i></div></article>
  </div>
</main>

<svg class="more" viewBox="0 0 18 14" aria-hidden="true"><polyline points="2,3 9,10 16,3" fill="none" stroke="#9aa49f" stroke-width="2"/></svg>

<footer class="footer">
  <p>© 2019 Company Name. All rights reserved.</p>
  <div class="social"><i></i><i></i><i></i><i></i><i></i></div>
</footer>

</body>
</html>
```